DeedVault Site Introduction and overview Flyer

We need a flyer made that gives an over view of our business. We are a land and mineral records company based in Texas that provides data to many different industries. This should be a bi-fold flyer that measures a 6" x 6" square. The designs should incorporate our company colors with subtle uses of the brighter colors from our new website. Logo and new website pictures are uploaded below.
we would like for the inside left to contain a brief company description: " Since 2005, DeedVault has provided online access to courthouse records and mineral ownership data. Our data, search and order management tools allow you to quickly build and store chains of title, division orders and contact lists. No other website provides as comprehensive of a data set. Start searching DeedVault today.
The front should contain a relevant photo, logo and website name.
the back should contain our contact information and graphic.
the inside right should contain 5 major bullet points with appropriate icons. the bullet points will be:
1. County Courthouse Records Available in Texas, Colorado, New Mexico, and Oklahoma
2. Search all Texas counties at once with Broadscan Lookup
3. Search mineral ownership data from across the State of Texas
4. Download bulk mineral appraisal rolls
5. Plats available in select counties

Target Market(s)
Oil & Gas, Legal, Surveyors, Title, Real Estate, male and female
Industry/Entity Type
Business
Font styles to use
Colors
Designer to choose colors to be used in the design.
Requirements
Must have
- Simplicity.
- relevant colors/graphics

Nice to have
- we would like to have the graphic shown in the sitecapture 2 used, if possible

Should not have
- non-relevant colors, graphics

```html
<!DOCTYPE html>
<html lang="en">
<head>
<meta charset="utf-8">
<title>DeedVault Bi-fold Flyer – Back and Front</title>
<link rel="stylesheet" href="https://fonts.googleapis.com/css2?family=Lato:wght@400;700;900&family=Roboto:wght@400;500&display=swap">
<style>
  :root{
    --stage:#eef0f2;
    --paper:#ffffff;
    --navy:#021047;
    --brand-blue:#1f3a9e;
    --accent-blue:#2f5cff;
    --ink:#111111;
    --photo-grey-light:#d9d9d9;
    --photo-grey-dark:#6e6e6e;
    --sky-violet:#7f78b8;
    --sky-pink:#c45a7c;
    --plant-dark:#1c2340;
    --plant-lights:#b9935a;
  }
  html,body{margin:0;padding:0;overflow:hidden;}
  body{
    width:1200px;height:1014px;
    background:var(--stage);
    display:flex;align-items:center;justify-content:center;
  }
  .spread{width:1080px;height:540px;display:block;box-shadow:0 10px 30px rgba(0,0,0,.18);}
  .brand-name{font-family:"Lato",sans-serif;font-weight:900;fill:var(--brand-blue);}
  .contact-tag{font-family:"Roboto",sans-serif;font-weight:500;font-size:17px;fill:#fff;}
  .contact-line{font-family:"Roboto",sans-serif;font-size:14px;fill:var(--ink);}
  .panel-email{font-family:"Lato",sans-serif;font-size:15px;fill:#dfe4ff;letter-spacing:.3px;}
  .cover-title{font-family:"Lato",sans-serif;font-weight:700;font-size:27px;fill:#fff;letter-spacing:-.3px;}
  .cover-subtitle{font-family:"Lato",sans-serif;font-weight:700;font-size:17px;fill:#fff;letter-spacing:.2px;}
</style>
</head>
<body>
<svg class="spread" viewBox="0 0 1080 540" xmlns="http://www.w3.org/2000/svg">
  <defs>
    <linearGradient id="greyPhotoTone" x1="0" y1="0" x2="0" y2="1">
      <stop offset="0" stop-color="var(--photo-grey-light)"/>
      <stop offset="1" stop-color="var(--photo-grey-dark)"/>
    </linearGradient>
    <linearGradient id="plantPhotoTone" x1="0" y1="0" x2="0.3" y2="1">
      <stop offset="0" stop-color="var(--sky-violet)"/>
      <stop offset="0.45" stop-color="var(--sky-pink)"/>
      <stop offset="0.7" stop-color="var(--plant-dark)"/>
      <stop offset="1" stop-color="var(--plant-lights)"/>
    </linearGradient>
  </defs>

  <!-- Back panel -->
  <g class="back-panel">
    <rect class="paper" x="0" y="0" width="540" height="540" fill="var(--paper)"/>
    <polygon class="navy-top-wedge" points="260,0 540,0 430,175" fill="var(--navy)"/>
    <polygon class="navy-bottom-wedge" points="330,330 540,540 140,540" fill="var(--navy)"/>
    <line x1="260" y1="0" x2="430" y2="175" stroke="var(--accent-blue)" stroke-width="4"/>
    <line x1="330" y1="330" x2="140" y2="540" stroke="var(--accent-blue)" stroke-width="4"/>

    <g class="brand-lockup">
      <rect x="40" y="58" width="20" height="20" fill="var(--brand-blue)"/>
      <text class="brand-name" x="68" y="76" font-size="24">DeedVault</text>
    </g>

    <g class="contact-block">
      <rect x="42" y="352" width="104" height="26" fill="var(--navy)"/>
      <text class="contact-tag" x="50" y="371">contact us</text>
      <path d="M52 392a5 5 0 0 1 10 0c0 4-5 9-5 9s-5-5-5-9z" fill="var(--ink)"/>
      <text class="contact-line" x="68" y="400">4780 Cedar Ridge Blvd</text>
      <text class="contact-line" x="68" y="418">Suite 310</text>
      <text class="contact-line" x="68" y="436">Amberton, TX 75990</text>
      <rect x="51" y="445" width="12" height="9" rx="1.5" fill="none" stroke="var(--ink)" stroke-width="1.6"/>
      <path d="M51 446l6 4 6-4" fill="none" stroke="var(--ink)" stroke-width="1.4"/>
      <text class="contact-line" x="68" y="455">info@deedvault.com</text>
      <path d="M53 464c1-1 3-1 3 1l-1 2c1 2 2 3 4 4l2-1c2 0 2 2 1 3-3 3-10-4-9-9z" fill="var(--ink)"/>
      <text class="contact-line" x="68" y="475">(555) 014-2290</text>
    </g>

    <text class="panel-email" x="300" y="505">info@deedvault.com</text>
  </g>

  <!-- Grey industrial photo spanning the fold -->
  <polygon class="refinery-photo" role="img" aria-label="Greyscale photo of a refinery with a tall striped smokestack"
           points="540,0 330,330 540,540 780,320 660,160" fill="url(#greyPhotoTone)"/>

  <!-- Front panel -->
  <g class="front-panel">
    <polygon class="logo-corner" points="540,0 790,0 660,160" fill="var(--paper)"/>
    <polygon class="plant-photo" role="img" aria-label="Photo of a power plant with three tall chimneys at dusk, mountains and harbour lights"
             points="790,0 1080,0 1080,540 1000,540 780,320 660,160" fill="url(#plantPhotoTone)"/>
    <polygon class="navy-front-wedge" points="780,320 540,540 1000,540" fill="var(--navy)"/>
    <line x1="790" y1="0" x2="660" y2="160" stroke="var(--accent-blue)" stroke-width="4"/>
    <line x1="780" y1="320" x2="540" y2="540" stroke="var(--accent-blue)" stroke-width="4"/>
    <line x1="780" y1="320" x2="1000" y2="540" stroke="var(--accent-blue)" stroke-width="3"/>

    <g class="brand-lockup">
      <rect x="602" y="42" width="16" height="16" fill="var(--brand-blue)"/>
      <text class="brand-name" x="624" y="57" font-size="19">DeedVault</text>
    </g>

    <text class="cover-title" x="1055" y="62" text-anchor="end">LAND AND MINERAL</text>
    <text class="cover-subtitle" x="1010" y="86" text-anchor="end">RECORDS COMPANY</text>

    <text class="panel-email" x="780" y="505" text-anchor="middle">info@deedvault.com</text>
  </g>

  <line class="fold" x1="540" y1="0" x2="540" y2="540" stroke="rgba(0,0,0,.08)" stroke-width="1"/>
</svg>
</body>
</html>
```